Real Estate Open House A Frame Sign

The sign is 22" wide and 28" tall. This sign is used to post around the neighbourhood to direct people to an open house (home that is for sale). It is also used for self-promotion.

Designwise
- I just want something with a modern look, simple and clean.
- I want my picture and business logo on the left side.
- On the right side, website (www.brindle-realestate.com) and my phone (510-364-2918), then a blank space where I can write an address when I need to.

I'm not sure how I want the overall design look. I'm very open-minded and I'm depending on your creative mind to come up with something.

If you have any questions, please let me know.

```html
<!DOCTYPE html>
<html lang="en">
<head>
<meta charset="utf-8">
<title>Open House A-Frame Sign</title>
<link rel="stylesheet" href="https://fonts.googleapis.com/css2?family=Lato:wght@400;700;900&display=swap">
<style>
  :root {
    --page-bg: #e9ecef;
    --sign-white: #ffffff;
    --brand-blue: #1b4585;
    --brand-blue-light: #2d5aa0;
    --panel-grey: #cbcbcb;
    --panel-grey-edge: #dedede;
    --photo-dark: #3a3f46;
    --photo-light: #c9cdd2;
  }
  html, body {
    margin: 0;
    padding: 0;
    width: 1200px;
    height: 800px;
    overflow: hidden;
    background: var(--page-bg);
  }
  .canvas {
    width: 1200px;
    height: 800px;
    display: flex;
    align-items: center;
    justify-content: center;
  }
  .sign {
    width: 581px;
    height: 738px;
    display: block;
    box-shadow: 0 6px 24px rgba(0,0,0,0.18);
    font-family: 'Lato', sans-serif;
  }
  .headline { font-weight: 900; fill: var(--brand-blue); }
  .brand-name { font-weight: 400; fill: var(--sign-white); }
  .contact { font-weight: 700; fill: var(--brand-blue); }
</style>
</head>
<body>
<main class="canvas">
  <svg class="sign" viewBox="0 0 740 940" xmlns="http://www.w3.org/2000/svg">
    <defs>
      <linearGradient id="agentTone" x1="0" y1="0" x2="0" y2="1">
        <stop offset="0" stop-color="var(--photo-light)"/>
        <stop offset="0.35" stop-color="#8a8f96"/>
        <stop offset="1" stop-color="var(--photo-dark)"/>
      </linearGradient>
    </defs>

    <rect class="sign-base" x="0" y="0" width="740" height="940" fill="var(--sign-white)"/>

    <!-- agent portrait area -->
    <path class="agent-portrait" role="img" aria-label="Portrait photo of the agent in a dark suit, arms crossed"
          d="M20 10 H330 V280 L470 420 L480 740 L0 740 V300 Z" fill="url(#agentTone)"/>

    <!-- headline -->
    <text class="headline" x="680" y="128" font-size="108" text-anchor="end">OPEN</text>
    <text class="headline" x="718" y="229" font-size="108" text-anchor="end">HOUSE</text>

    <!-- grey lower panel -->
    <polygon class="grey-edge" points="740,400 740,416 290,752 268,752" fill="var(--panel-grey-edge)"/>
    <polygon class="grey-panel" points="740,416 740,940 150,940 290,752" fill="var(--panel-grey)"/>

    <!-- blue corner band -->
    <polygon class="blue-stripe" points="0,572 0,588 545,940 520,940" fill="var(--brand-blue-light)"/>
    <polygon class="blue-band" points="0,590 0,940 552,940" fill="var(--brand-blue)"/>

    <!-- brand name -->
    <text class="brand-name" x="34" y="866" font-size="68" letter-spacing="2">BRINDLE</text>
    <text class="brand-name" x="36" y="898" font-size="19" letter-spacing="6.5">REAL ESTATE</text>

    <!-- contact -->
    <text class="contact" x="716" y="840" font-size="21.5" text-anchor="end">www.brindle-realestate.com</text>
    <g class="phone-icon" transform="translate(506 863)">
      <circle r="11" fill="var(--brand-blue)"/>
      <path d="M-5 -5 q1 -2 3 -1 l2 3 q0 1 -1 2 q1 3 4 4 q1 -1 2 -1 l3 2 q1 2 -1 3 q-3 2 -8 -2 q-5 -5 -4 -10 z" fill="var(--sign-white)"/>
    </g>
    <text class="contact" x="716" y="874" font-size="30" text-anchor="end">510-364-2918</text>
  </svg>
</main>
</body>
</html>
```